Website Design Brief for KTR LEGAL PTY LTD

Company Name: KTR LEGAL PTY LTD

Industry: Legal Services

Target Audience:

Corporate clients
Business owners
Individuals seeking legal advice in Commercial Law, Mergers and Acquisitions, Will Law, Property Law, and Conveyancing
Objective:

To create a professional, user-friendly website that establishes trust and authority in the legal field.
Provide easy access to information about the firm’s services, team, and areas of expertise.
Include client testimonials, contact information, and a blog or resource section for legal insights.
Key Features and Pages:

Homepage:

Clean, modern design with a professional feel.
Introduction to KTR LEGAL with a brief overview of services.
High-quality images or illustrations related to law and professionalism.
Prominent call-to-action (CTA) like "Get in Touch" or "Book a Consultation."
About Us:

Information about the firm's mission, values, and team.
Highlight the expertise and experience of key members.
Include a brief company history, if relevant.
Services:

Detailed descriptions of services, categorized by legal areas (e.g., Commercial Law, Mergers & Acquisitions, Property Law, etc.).
Call-to-action buttons to encourage potential clients to reach out for consultations.
Team:

Profiles of key team members, including their qualifications, expertise, and professional photos.
Include links to their professional networks (LinkPlaza).
Testimonials:

Section showcasing positive client testimonials or case studies.
This can help build trust and credibility with potential clients.
Blog or Resources:

A blog or resources section providing legal tips, industry news, and insights.
Content should demonstrate the firm’s knowledge and thought leadership.
Contact Us:

Easy-to-use contact form.
Include phone number, email, physical office address, and possibly a map.
Option for booking consultations or initial meetings directly online.
Client Portal (optional):

Secure login for clients to access their case information, documents, and updates (this could be an advanced feature to consider after launch).
Design Aesthetic:

Clean, modern, and professional.
Elegant use of fonts and a color palette that reflects trust, authority, and sophistication (dark blues, whites, grays).
User-friendly navigation to ensure clients can easily find the information they need.
Technical Considerations:

The website should be mobile-responsive and look great on all devices (desktop, tablet, mobile).
Ensure fast load times and optimized images.
Implement SEO best practices to improve search engine rankings.
Easy-to-update CMS (WordPress or similar) to allow easy future updates.
Competitor/Inspirational Websites:

[Provide examples of legal firms' websites you like, or any designs that reflect the feel you want for your firm.]
Additional Information:

Please ensure all content is aligned with the firm's professional tone and approach.
The website should be designed to be scalable for future growth (adding more services, resources, etc.).

Target Market(s)

Business owners Individuals seeking legal advice in Commercial Law, Mergers and Acquisitions, Will Law, Property Law, and Conveyancing

Industry/Entity Type

Legal

Number of Pages Required

3 page

Requirements
Must have
• Home Page, About Us, Contact Us, Services

```html
<!DOCTYPE html>
<html lang="en">
<head>
<meta charset="utf-8">
<title>KTR LEGAL — Legal Services</title>
<link href="https://fonts.googleapis.com/css2?family=Montserrat:wght@300;400;500;600;700;800&family=Josefin+Sans:ital,wght@0,300;0,400;0,600;1,300;1,400&display=swap" rel="stylesheet">
<style>
:root{
  --ink:#0d0d0d;
  --black:#000;
  --white:#fff;
  --paper:#f7f7f7;
  --card:#f1f1f1;
  --field:#f0f0f0;
  --grey:#777;
  --muted:#9a9a9a;
  --line:#3a3a3a;
  --gold:#f2b01e;
  --hero-a:#2a1d14;
  --hero-b:#5a4330;
}
*{margin:0;padding:0;box-sizing:border-box}
html,body{width:1200px;height:4800px;overflow:hidden;background:var(--white)}
body{position:relative;font-family:"Josefin Sans",sans-serif;color:var(--ink)}
.abs{position:absolute}
.head{font-family:"Montserrat",sans-serif}

/* hero */
.hero{left:0;top:0;width:1200px;height:598px;background:linear-gradient(120deg,var(--hero-a),var(--hero-b) 45%,#1f1812 80%,#120d09)}
.hero-shade{left:0;top:0;width:1200px;height:598px;background:rgba(0,0,0,.38)}
.nav-bar{left:138px;top:35px;width:924px;height:67px}
.brand-name{font-family:"Montserrat",sans-serif;font-size:26px;font-weight:500;letter-spacing:0;color:var(--ink);white-space:nowrap}
.nav-link{top:61px;font-family:"Montserrat",sans-serif;font-size:12px;font-weight:500;color:var(--ink)}
.nav-cta{left:810px;top:50px;width:224px;height:40px;background:var(--black);color:var(--white);font-family:"Montserrat",sans-serif;font-size:12px;font-weight:600;display:flex;align-items:center;justify-content:center}
.welcome{left:0;width:1200px;top:206px;text-align:center;color:var(--white);font-family:"Montserrat",sans-serif;font-size:22px;letter-spacing:6px;font-weight:400}
.hero-title{left:0;width:1200px;top:228px;text-align:center;color:var(--white);font-family:"Montserrat",sans-serif;font-size:100px;line-height:1.1;font-weight:500;letter-spacing:-1px}
.hero-copy{left:230px;width:740px;top:352px;text-align:center;color:var(--white);font-size:16px;line-height:28px}
.hero-cta{left:486px;top:427px;width:209px;height:36px;background:var(--black);color:var(--white);font-family:"Montserrat",sans-serif;font-size:12px;font-weight:600;display:flex;align-items:center;justify-content:center}
.dot{top:558px;height:3px;background:rgba(255,255,255,.35)}
.dot.on{background:var(--white)}

/* about */
.about-photo{left:0;top:598px;width:624px;height:520px;background:linear-gradient(135deg,#d9d4cb,#8e8a84 45%,#2c3544 75%,#ece7df);clip-path:polygon(0 0,531px 0,624px 520px,0 520px)}
.eyebrow{font-family:"Montserrat",sans-serif;font-size:15px;letter-spacing:3px;font-weight:500;color:var(--ink)}
.h2{font-family:"Montserrat",sans-serif;font-size:50px;line-height:1;color:var(--ink);letter-spacing:-.5px}
.h2 b{font-weight:800}
.h2 span{font-weight:300}
.rule{height:3px;background:var(--ink)}
.body-copy{font-size:16px;line-height:28px;color:var(--grey)}
.center{left:0;width:1200px;text-align:center}

/* services */
.band{left:0;width:1200px;background:var(--paper)}
.svc{top:1369px;width:287px;height:317px}
.svc-shape{left:0;top:0;width:287px;height:317px}
.svc-icon{left:100px;top:0;width:87px;height:87px}
.svc-title{left:0;width:287px;top:108px;text-align:center;font-family:"Montserrat",sans-serif;font-weight:600;font-size:18px}
.svc-copy{left:10px;width:267px;top:136px;text-align:center;font-size:16px;line-height:28px;color:var(--grey)}
.svc-btn{left:70px;top:248px;width:140px;height:38px}

/* team */
.member{top:2040px;width:228px;height:291px;background:var(--card)}
.member.active{background:var(--black)}
.portrait{left:34px;top:33px;width:160px;height:160px;border-radius:50%;background:linear-gradient(160deg,#e9e4dc,#8a8f98 55%,#2e3440)}
.m-name{left:0;width:228px;top:214px;text-align:center;font-family:"Montserrat",sans-serif;font-weight:600;font-size:18px;color:var(--ink);white-space:nowrap}
.m-role{left:0;width:228px;top:248px;text-align:center;font-size:14px;color:var(--muted)}
.member.active .m-name,.member.active .m-role{color:var(--white)}

/* testimonials */
.review{top:2599px;width:442px;height:268px;background:var(--paper)}
.review.lift{background:var(--white);box-shadow:0 4px 22px rgba(0,0,0,.13)}
.r-text{left:24px;top:18px;width:398px;font-style:italic;font-weight:300;font-size:15.5px;line-height:28px;color:var(--grey)}
.r-avatar{left:24px;top:171px;width:72px;height:72px;border-radius:50%;background:linear-gradient(160deg,#d8d2c8,#5b5f67 60%,#23272e)}
.r-name{left:112px;top:184px;font-family:"Montserrat",sans-serif;font-weight:500;font-size:17px}
.r-stars{left:112px;top:210px;color:var(--gold);font-size:12px;letter-spacing:1px}
.r-quote{left:330px;top:170px;width:92px;height:72px}
.arrow{top:2717px;width:20px;height:32px}

/* resources */
.post{top:3214px;width:293px;height:354px;border:2px solid var(--line);background:var(--white)}
.post-img{left:10px;top:10px;width:269px;height:236px}
.post-title{left:14px;top:262px;width:265px;font-size:18px;line-height:30px;color:var(--ink)}
.post-meta{left:14px;top:325px;font-size:13px;color:var(--muted)}

/* contact */
.field{left:143px;width:366px;background:var(--field);font-size:14px;color:var(--grey);padding:16px 0 0 20px}
.map{left:600px;top:3910px;width:454px;height:403px;background:linear-gradient(135deg,#e6e6e6,#d4d4d4 50%,#e9e9e9)}
.addr-card{left:700px;top:4074px;width:258px;height:108px;background:var(--white);border-radius:10px;box-shadow:0 4px 16px rgba(0,0,0,.15)}

/* footer */
.footer{left:0;top:4406px;width:1200px;height:394px;background:var(--black);color:var(--white)}
.social{top:4600px;width:22px;height:22px;border-radius:50%;border:1.5px solid var(--white)}
.f-head{font-family:"Montserrat",sans-serif;font-size:24px;font-weight:500;color:var(--white)}
.f-link{font-size:16px;color:var(--white)}
.f-rule{left:140px;top:4700px;width:915px;height:1px;background:rgba(255,255,255,.45)}
.copyright{left:0;width:1200px;top:4730px;text-align:center;font-size:14px;color:var(--white)}
</style>
</head>
<body>

<!-- Hero -->
<section class="abs hero" role="img" aria-label="Photograph of a lawyer standing in a wood-panelled courtroom"></section>
<div class="abs hero-shade"></div>
<svg class="abs nav-bar" width="924" height="67" viewBox="0 0 924 67"><polygon points="0,0 886,0 924,67 0,67" fill="#fff"/></svg>
<div class="abs brand-name" style="left:147px;top:53px">KTR LEGAL</div>
<a class="abs nav-link" style="left:367px">HOME</a>
<a class="abs nav-link" style="left:451px">ABOUT US</a>
<a class="abs nav-link" style="left:561px">CONTACT US</a>
<a class="abs nav-link" style="left:687px">SERVICES</a>
<div class="abs nav-cta">SCHEDULE A CONSULTATION</div>
<div class="abs welcome">WELCOME TO</div>
<h1 class="abs hero-title">KTR LEGAL</h1>
<p class="abs hero-copy">Lorem ipsum dolor sit amet, consectetur adipiscing elit, sed do eiusmod tempor incididunt ut labore et dolore magna aliquar maecenas accumsan lacus vel facilisis.</p>
<div class="abs hero-cta">SCHEDULE A CONSULTATION</div>
<div class="abs dot on" style="left:522px;width:60px"></div>
<div class="abs dot" style="left:586px;width:28px"></div>
<div class="abs dot" style="left:618px;width:28px"></div>
<div class="abs dot" style="left:650px;width:28px"></div>

<!-- About -->
<div class="abs about-photo" role="img" aria-label="Photograph of a lawyer at her desk holding a pen, scales of justice behind her"></div>
<div class="abs eyebrow" style="left:663px;top:668px">WHO WE ARE</div>
<h2 class="abs h2" style="left:663px;top:694px;font-size:48px"><b>ABOUT</b> <span>KTR LEGAL</span></h2>
<div class="abs rule" style="left:663px;top:744px;width:186px"></div>
<p class="abs body-copy" style="left:663px;top:792px;width:480px">Lorem ipsum dolor sit amet, consectetur adipiscing elit, sed do eiusmod tempor incididunt ut labore et dolore magna aliquar maecenas accumsan lacus vel facilisised ut perspiciatis unde omnis iste natus error sit voluptatem accusantium doloremque laudantium, totam rem aperiam, eaque ipsa quae ab illo inventore veritatis et quasi architecto beatae vitae dicta sunt explicabo quaerat voluptatem.</p>
<svg class="abs" style="left:665px;top:1006px" width="130" height="39" viewBox="0 0 130 39"><polygon points="0,0 108,0 130,39 0,39" fill="#000"/><text x="14" y="24" fill="#fff" font-family="Montserrat,sans-serif" font-size="12" font-weight="600">LEARN MORE</text></svg>

<!-- Services -->
<section class="abs band" style="top:1118px;height:667px"></section>
<div class="abs eyebrow center" style="top:1217px">OUR SERVICES</div>
<h2 class="abs h2 center" style="top:1243px"><b>WHAT WE</b> <span>SERVICES</span></h2>
<div class="abs rule" style="left:516px;top:1303px;width:170px"></div>

<div class="abs svc" style="left:145px">
  <svg class="abs svc-shape" viewBox="0 0 287 317"><polygon points="0,12 287,60 287,317 0,317" fill="#fff"/></svg>
  <svg class="abs svc-icon" viewBox="0 0 87 87"><circle cx="43.5" cy="43.5" r="41" fill="#fff" stroke="#111" stroke-width="2" stroke-dasharray="5 4"/><rect x="31" y="26" width="22" height="32" fill="none" stroke="#111" stroke-width="2"/><line x1="36" y1="34" x2="48" y2="34" stroke="#111" stroke-width="2"/><line x1="36" y1="40" x2="48" y2="40" stroke="#111" stroke-width="2"/><line x1="36" y1="46" x2="44" y2="46" stroke="#111" stroke-width="2"/><line x1="46" y1="56" x2="58" y2="40" stroke="#111" stroke-width="3"/></svg>
  <div class="abs svc-title">COMMERCIAL LAW</div>
  <p class="abs svc-copy">Lorem ipsum dolor sit amet, consectetur adipiscing elit, sed do eiusmod tempo.</p>
  <svg class="abs svc-btn" viewBox="0 0 140 38"><polygon points="1,1 118,1 138,37 1,37" fill="none" stroke="#111" stroke-width="1.5"/><text x="14" y="24" fill="#111" font-family="Montserrat,sans-serif" font-size="11.5" font-weight="600">LEARN MORE</text></svg>
</div>

<div class="abs svc" style="left:456px">
  <svg class="abs svc-shape" viewBox="0 0 287 317" style="filter:drop-shadow(0 4px 10px rgba(0,0,0,.12))"><polygon points="0,12 287,60 287,317 0,317" fill="#fff"/><rect x="0" y="311" width="287" height="6" fill="#000"/></svg>
  <svg class="abs svc-icon" viewBox="0 0 87 87"><circle cx="43.5" cy="43.5" r="42" fill="#000"/><path d="M26 44 L36 34 L44 40 L52 34 L62 44 L50 56 L38 56 Z" fill="none" stroke="#fff" stroke-width="2.5" stroke-linejoin="round"/><line x1="40" y1="46" x2="46" y2="52" stroke="#fff" stroke-width="2"/></svg>
  <div class="abs svc-title">MERGERS &amp; ACQUISITIONS</div>
  <p class="abs svc-copy">Lorem ipsum dolor sit amet, consectetur adipiscing elit, sed do eiusmod tempo.</p>
  <svg class="abs svc-btn" viewBox="0 0 140 38"><polygon points="0,0 118,0 140,38 0,38" fill="#000"/><text x="14" y="24" fill="#fff" font-family="Montserrat,sans-serif" font-size="11.5" font-weight="600">LEARN MORE</text></svg>
</div>

<div class="abs svc" style="left:769px">
  <svg class="abs svc-shape" viewBox="0 0 287 317"><polygon points="0,12 287,60 287,317 0,317" fill="#fff"/></svg>
  <svg class="abs svc-icon" viewBox="0 0 87 87"><circle cx="43.5" cy="43.5" r="41" fill="#fff" stroke="#111" stroke-width="2" stroke-dasharray="5 4"/><path d="M26 46 L43.5 28 L61 46" fill="none" stroke="#111" stroke-width="2.5"/><rect x="32" y="44" width="23" height="16" fill="none" stroke="#111" stroke-width="2.5"/><rect x="40" y="50" width="7" height="10" fill="#111"/></svg>
  <div class="abs svc-title">PROPERTY LAW</div>
  <p class="abs svc-copy">Lorem ipsum dolor sit amet, consectetur adipiscing elit, sed do eiusmod tempo.</p>
  <svg class="abs svc-btn" viewBox="0 0 140 38"><polygon points="1,1 118,1 138,37 1,37" fill="none" stroke="#111" stroke-width="1.5"/><text x="14" y="24" fill="#111" font-family="Montserrat,sans-serif" font-size="11.5" font-weight="600">LEARN MORE</text></svg>
</div>

<!-- Team -->
<div class="abs eyebrow center" style="top:1903px">OUR TEAM</div>
<h2 class="abs h2 center" style="top:1929px"><b>MEET</b> <span>OUR EXPERTISE</span></h2>
<div class="abs rule" style="left:516px;top:1989px;width:170px"></div>

<div class="abs member" style="left:116px"><div class="abs portrait" role="img" aria-label="Portrait photo of a team member with a tablet"></div><div class="abs m-name">DANIEL WHITFORD</div><div class="abs m-role">LAYWER</div></div>
<div class="abs member active" style="left:363px"><div class="abs portrait" role="img" aria-label="Portrait photo of a team member in a dark suit"></div><div class="abs m-name">DANIEL WHITFORD</div><div class="abs m-role">LAYWER</div></div>
<div class="abs member" style="left:609px"><div class="abs portrait" role="img" aria-label="Portrait photo of a team member in a blue suit"></div><div class="abs m-name">DANIEL WHITFORD</div><div class="abs m-role">LAYWER</div></div>
<div class="abs member" style="left:855px"><div class="abs portrait" role="img" aria-label="Portrait photo of a team member in a pink blazer"></div><div class="abs m-name">DANIEL WHITFORD</div><div class="abs m-role">LAYWER</div></div>

<!-- Testimonials -->
<div class="abs eyebrow center" style="top:2458px">OUR REVIEWS</div>
<h2 class="abs h2 center" style="top:2484px"><b>TESTIMONIALS</b> <span>&amp; CASE STUDIES</span></h2>
<div class="abs rule" style="left:516px;top:2546px;width:170px"></div>

<svg class="abs arrow" style="left:92px" viewBox="0 0 20 32"><polyline points="16,2 4,16 16,30" fill="none" stroke="#111" stroke-width="2.5"/></svg>
<svg class="abs arrow" style="left:1089px" viewBox="0 0 20 32"><polyline points="4,2 16,16 4,30" fill="none" stroke="#111" stroke-width="2.5"/></svg>

<div class="abs review lift" style="left:143px">
  <p class="abs r-text">Lorem ipsum dolor sit amet, consectetur adipiscing elit, sed do eiusmod tempor incididunt ut labore et dolore magna aliqua. Quis ipsum suspendisse ultrices gravida. Risus commodo viverra maecenas accumsan lacus vel facilisis.</p>
  <div class="abs r-avatar" role="img" aria-label="Client portrait photo"></div>
  <div class="abs r-name">Aaron Miles</div>
  <div class="abs r-stars">★★★★★</div>
  <svg class="abs r-quote" viewBox="0 0 92 72"><path d="M4 70 L20 4 L42 4 L30 70 Z M50 70 L66 4 L88 4 L76 70 Z" fill="#e4e4e4"/></svg>
</div>
<div class="abs review" style="left:613px">
  <p class="abs r-text">Lorem ipsum dolor sit amet, consectetur adipiscing elit, sed do eiusmod tempor incididunt ut labore et dolore magna aliqua. Quis ipsum suspendisse ultrices gravida. Risus commodo viverra maecenas accumsan lacus vel facilisis.</p>
  <div class="abs r-avatar" role="img" aria-label="Client portrait photo"></div>
  <div class="abs r-name">Aaron Miles</div>
  <div class="abs r-stars">★★★★★</div>
  <svg class="abs r-quote" viewBox="0 0 92 72"><path d="M4 70 L20 4 L42 4 L30 70 Z M50 70 L66 4 L88 4 L76 70 Z" fill="#e4e4e4"/></svg>
</div>

<!-- Resources -->
<section class="abs band" style="top:2994px;height:667px"></section>
<div class="abs eyebrow center" style="top:3086px">OUR INSIGHTS</div>
<h2 class="abs h2 center" style="top:3112px"><b>OUR LATEST</b> <span>RESOURCES</span></h2>
<div class="abs rule" style="left:516px;top:3174px;width:170px"></div>

<article class="abs post" style="left:143px"><div class="abs post-img" role="img" aria-label="Photo of a lawyer working on a laptop" style="background:linear-gradient(135deg,#eceae6,#b9b5ae 55%,#4a4d52)"></div><div class="abs post-title">Ut enim ad minima veniam quis nostrum exerc.</div><div class="abs post-meta">&#9679; By Admin &nbsp; &#9633; Mar 24 2025</div></article>
<article class="abs post" style="left:453px"><div class="abs post-img" role="img" aria-label="Photo of a team meeting around a table" style="background:linear-gradient(135deg,#7a5a3e,#c9b59b 50%,#3b3f48)"></div><div class="abs post-title">Ut enim ad minima veniam quis nostrum exerc.</div><div class="abs post-meta">&#9679; By Admin &nbsp; &#9633; Mar 24 2025</div></article>
<article class="abs post" style="left:762px"><div class="abs post-img" role="img" aria-label="Photo of a handshake in an office" style="background:linear-gradient(135deg,#2e3540,#8c939c 55%,#d8dadd)"></div><div class="abs post-title">Ut enim ad minima veniam quis nostrum exerc.</div><div class="abs post-meta">&#9679; By Admin &nbsp; &#9633; Mar 24 2025</div></article>

<!-- Contact -->
<div class="abs eyebrow center" style="top:3769px">CONTACT US</div>
<h2 class="abs h2 center" style="top:3795px"><b>REQUEST A</b> <span>CONSULTATIONS</span></h2>
<div class="abs rule" style="left:516px;top:3855px;width:170px"></div>

<div class="abs field" style="top:3921px;height:44px">Full Name</div>
<div class="abs field" style="top:3977px;height:45px">Email Address</div>
<div class="abs field" style="top:4033px;height:45px">Phone Number</div>
<div class="abs field" style="top:4089px;height:146px">Messsage</div>
<svg class="abs" style="left:143px;top:4262px" width="140" height="43" viewBox="0 0 140 43"><polygon points="0,0 118,0 140,43 0,43" fill="#000"/><text x="14" y="26" fill="#fff" font-family="Montserrat,sans-serif" font-size="12" font-weight="600">SUBMIT NOW</text></svg>

<div class="abs map" role="img" aria-label="Street map showing the office location"></div>
<div class="abs addr-card">
  <svg class="abs" style="left:18px;top:32px" width="40" height="44" viewBox="0 0 40 44"><path d="M20 4 C12 4 7 10 7 16 C7 25 20 36 20 36 C20 36 33 25 33 16 C33 10 28 4 20 4 Z" fill="none" stroke="#111" stroke-width="2"/><circle cx="20" cy="16" r="5" fill="none" stroke="#111" stroke-width="2"/><path d="M2 42 L10 30 M38 42 L30 30 M2 42 L38 42" stroke="#111" stroke-width="2" fill="none"/></svg>
  <div class="abs head" style="left:76px;top:20px;font-size:15px;font-weight:500">ADDRESS</div>
  <div class="abs" style="left:76px;top:46px;font-size:12px;line-height:24px;color:var(--grey)">48 Harbour Lane, Easton,<br>united state - 204 118.</div>
</div>

<!-- Footer -->
<footer class="abs footer"></footer>
<div class="abs brand-name" style="left:143px;top:4535px;color:var(--white);font-size:28px">KTR LEGAL</div>
<div class="abs social" style="left:164px" aria-label="Social profile"></div>
<div class="abs social" style="left:205px" aria-label="Social profile"></div>
<div class="abs social" style="left:244px" aria-label="Social profile"></div>
<div class="abs social" style="left:283px" aria-label="LinkPlaza profile"></div>

<div class="abs f-head" style="left:397px;top:4470px">Quick Links</div>
<div class="abs f-link" style="left:397px;top:4518px">Home</div>
<div class="abs f-link" style="left:397px;top:4550px">About us</div>
<div class="abs f-link" style="left:397px;top:4581px">Contact us</div>
<div class="abs f-link" style="left:397px;top:4613px">Services</div>
<div class="abs f-link" style="left:397px;top:4645px">Testimonials</div>

<div class="abs f-head" style="left:602px;top:4470px">Legal</div>
<div class="abs f-link" style="left:602px;top:4518px">Privacy Policy</div>
<div class="abs f-link" style="left:602px;top:4550px">Terms &amp; Conditions</div>
<div class="abs f-link" style="left:602px;top:4581px">Sitemap</div>
<div class="abs f-link" style="left:602px;top:4613px">Team</div>

<div class="abs f-head" style="left:822px;top:4470px">Contact details</div>
<svg class="abs" style="left:822px;top:4518px" width="12" height="16" viewBox="0 0 12 16"><path d="M6 0 C2.7 0 0 2.6 0 5.8 C0 10 6 16 6 16 C6 16 12 10 12 5.8 C12 2.6 9.3 0 6 0 Z" fill="#fff"/><circle cx="6" cy="6" r="2.2" fill="#000"/></svg>
<div class="abs f-link" style="left:848px;top:4518px;line-height:32px">48 Harbour Lane, Easton,<br>united state - 204 118.</div>
<svg class="abs" style="left:821px;top:4591px" width="15" height="11" viewBox="0 0 15 11"><rect width="15" height="11" fill="#fff"/><polyline points="0,0 7.5,6 15,0" fill="none" stroke="#000" stroke-width="1.4"/></svg>
<div class="abs f-link" style="left:848px;top:4588px">hello@ktrlegalmail.com</div>
<svg class="abs" style="left:822px;top:4630px" width="13" height="13" viewBox="0 0 13 13"><path d="M2.5 0.5 L5 3.5 L3.6 5.2 C4.4 7 6 8.6 7.8 9.4 L9.5 8 L12.5 10.5 L11 12.5 C5.5 12.5 0.5 7.5 0.5 2 Z" fill="#fff"/></svg>
<div class="abs f-link" style="left:848px;top:4627px">+123 555 0190</div>

<div class="abs f-rule"></div>
<div class="abs copyright">2025 Copyrights © &nbsp;KTR LEGAL PTY LTD &nbsp;| &nbsp;All Rights Reserved</div>

</body>
</html>
```